Brightpath Strategic Advisers F.Z.E
Professional
Khalid Yousef Nasser
Founder & CEO
Corvana Trade Park
info@bsa-qx.com
www.bsa-qx.com
Training & Consultancy on:
QBXR Assessment & Training
Leadership Development & Coaching
Change Management
Strategy Management
Performance Management
Quality & Process Management
TQM
HR Development
HR Procedures & Regulation
Logo & Full Stationeries & P.P Presentation first page and continues sheet & Proposal document cover & continues sheet

```html
<!DOCTYPE html>
<html lang="en">
<head>
<meta charset="utf-8">
<title>Brightpath Strategic Advisers – Business Card</title>
<link href="https://fonts.googleapis.com/css2?family=Open+Sans:wght@400;600;700&display=swap" rel="stylesheet">
<style>
  :root {
    --page-bg: #e9e6e1;
    --card-dark: #111111;
    --card-mid: #2b2b2b;
    --band-red: #d8231b;
    --band-orange: #f58220;
    --swoosh-grey: #5c5c5c;
    --text-white: #ffffff;
    --text-soft: #cfcfcf;
    --accent: #f58220;
  }
  html, body {
    margin: 0;
    padding: 0;
    width: 1200px;
    height: 780px;
    overflow: hidden;
    background: var(--page-bg);
    font-family: "Open Sans", Arial, sans-serif;
  }
  .canvas {
    position: relative;
    width: 1200px;
    height: 780px;
  }
  .business-card {
    position: absolute;
    left: 100px;
    top: 95px;
    width: 1000px;
    height: 590px;
    border-radius: 38px;
    overflow: hidden;
    background: radial-gradient(ellipse at 40% 55%, var(--card-mid) 0%, var(--card-dark) 75%);
    box-shadow: 0 10px 30px rgba(0,0,0,0.25);
  }
  .card-band {
    position: absolute;
    inset: 0;
    width: 1000px;
    height: 590px;
  }
  .holder {
    position: absolute;
    right: 62px;
    top: 42px;
    text-align: right;
    color: var(--text-white);
  }
  .holder-name {
    font-size: 31px;
    font-weight: 700;
    margin: 0;
    letter-spacing: 0.3px;
  }
  .holder-title {
    font-size: 21px;
    font-weight: 400;
    margin: 6px 0 0;
  }
  .company-mark {
    position: absolute;
    left: 82px;
    top: 250px;
    display: flex;
    align-items: flex-start;
    gap: 18px;
  }
  .company-square {
    width: 34px;
    height: 34px;
    background: var(--accent);
    margin-top: 6px;
  }
  .company-name {
    margin: 0;
    color: var(--text-white);
    font-size: 36px;
    font-weight: 600;
    line-height: 1.15;
    letter-spacing: 0.5px;
  }
  .contact {
    position: absolute;
    left: 70px;
    top: 410px;
    color: var(--text-soft);
    font-size: 19px;
  }
  .contact-address {
    margin: 0 0 16px;
  }
  .contact-list {
    list-style: none;
    margin: 0;
    padding: 0;
  }
  .contact-item {
    display: flex;
    align-items: center;
    gap: 12px;
    margin-bottom: 9px;
  }
  .contact-icon {
    width: 22px;
    height: 22px;
    flex: none;
  }
</style>
</head>
<body>
<main class="canvas">
  <section class="business-card" aria-label="Business card">
    <svg class="card-band" viewBox="0 0 1000 590" aria-hidden="true">
      <defs>
        <linearGradient id="bandGradient" x1="0" y1="0" x2="1" y2="0">
          <stop offset="0" stop-color="var(--band-red)"/>
          <stop offset="1" stop-color="var(--band-orange)"/>
        </linearGradient>
      </defs>
      <path d="M0 0 H1000 V100 C820 100 640 115 460 150 C300 182 150 205 0 215 Z" fill="url(#bandGradient)"/>
      <path d="M0 232 C150 222 300 198 460 166 C640 130 820 116 1000 116" fill="none" stroke="var(--swoosh-grey)" stroke-width="7"/>
    </svg>

    <div class="holder">
      <p class="holder-name">Khalid Yousef Nasser</p>
      <p class="holder-title">Founder &amp; CEO</p>
    </div>

    <div class="company-mark">
      <span class="company-square" aria-hidden="true"></span>
      <p class="company-name">BRIGHTPATH STRATEGIC<br>ADVISERS F.Z.E</p>
    </div>

    <div class="contact">
      <p class="contact-address">Corvana Trade Park</p>
      <ul class="contact-list">
        <li class="contact-item">
          <svg class="contact-icon" viewBox="0 0 22 22" aria-hidden="true">
            <rect x="5" y="1" width="12" height="20" rx="2.5" fill="var(--accent)"/>
            <rect x="7.5" y="4" width="7" height="10" fill="var(--card-dark)"/>
            <circle cx="11" cy="17.5" r="1.4" fill="var(--card-dark)"/>
          </svg>
          <span>00971558031746</span>
        </li>
        <li class="contact-item">
          <svg class="contact-icon" viewBox="0 0 22 22" aria-hidden="true">
            <rect x="1" y="4" width="20" height="14" rx="2" fill="var(--accent)"/>
            <path d="M2 5 L11 12 L20 5" fill="none" stroke="var(--card-dark)" stroke-width="2"/>
          </svg>
          <span>info@bsa-qx.com</span>
        </li>
        <li class="contact-item">
          <svg class="contact-icon" viewBox="0 0 22 22" aria-hidden="true">
            <rect x="1" y="3" width="20" height="16" rx="2" fill="var(--accent)"/>
            <rect x="3.5" y="7" width="15" height="9.5" fill="var(--card-dark)"/>
          </svg>
          <span>www.bsa-qx.com</span>
        </li>
      </ul>
    </div>
  </section>
</main>
</body>
</html>
```